Business card for Sports Apparel business

DOUBLE SIDED DESIGN
We need business cards for a new sports apparel business. We are developing a protective headband for soccer initially.
Corvell is focused on designing and developing head protection products to reduce the likelihood of concussion when playing sports. Exploring and understanding medical insights, material science research, current and former players experiences and governing bodies guidelines has allowed Corvell to develop the safety, style, form and function requirements of a suitable product to bring to market.
Target Market(s)
Mums buying kits for the sons and daughters. Amateur footballers.
Industry/Entity Type
Sporting Good
Contact Information for Business Card
Martin Ashgrove - CEO
Mobile: +44 7391608254
Email: martin@corvell.co.uk
Tel: 0208 5143927
Helena Pardoe - COO
Mob: +44 7356 409183
Email: helena@corvell.co.uk
Tel: 0208 5143927
Duncan Wyvern - CCO
Mob: +44 7468 230517
Email: duncan@corvell.co.uk
Tel: 0208 5143927
Look and feel

```html
<!DOCTYPE html>
<html lang="en">
<head>
<meta charset="utf-8">
<title>Corvell Business Card</title>
<link rel="stylesheet" href="https://fonts.googleapis.com/css2?family=Montserrat:wght@300;400;600;700&display=swap">
<style>
  :root {
    --backdrop: #262626;
    --card-grey: #676767;
    --card-white: #ffffff;
    --brand-blue: #145d96;
    --text-grey: #5d5d5d;
    --text-light: #ffffff;
  }
  * { margin: 0; padding: 0; box-sizing: border-box; }
  html, body {
    width: 1200px;
    height: 900px;
    overflow: hidden;
    background: var(--backdrop);
    font-family: "Montserrat", sans-serif;
  }
  .sheet {
    position: relative;
    width: 1200px;
    height: 900px;
  }
  .card {
    position: absolute;
    left: 290px;
    width: 620px;
    height: 354px;
    overflow: hidden;
  }
  .card-front {
    top: 76px;
    background: var(--card-grey);
    display: flex;
    align-items: center;
    justify-content: center;
  }
  .front-wordmark {
    color: var(--text-light);
    font-weight: 600;
    font-size: 66px;
    letter-spacing: 4px;
  }
  .card-back {
    top: 470px;
    background: var(--card-white);
  }
  .back-wave {
    position: absolute;
    inset: 0;
  }
  .back-wordmark {
    position: absolute;
    left: 44px;
    top: 44px;
    color: var(--text-grey);
    font-weight: 600;
    font-size: 36px;
    letter-spacing: 2px;
  }
  .holder {
    position: absolute;
    right: 36px;
    top: 110px;
    text-align: right;
  }
  .holder-name {
    color: var(--brand-blue);
    font-weight: 700;
    font-size: 17px;
    letter-spacing: 1px;
  }
  .holder-role {
    color: var(--text-grey);
    font-weight: 300;
    font-size: 14px;
    letter-spacing: 1px;
    margin-top: 2px;
  }
  .contacts {
    position: absolute;
    right: 36px;
    bottom: 26px;
    list-style: none;
    color: var(--text-light);
    font-weight: 300;
    font-size: 15px;
    line-height: 24px;
  }
  .contacts li {
    display: flex;
    justify-content: flex-end;
    align-items: center;
    gap: 12px;
  }
  .contacts svg {
    width: 14px;
    height: 14px;
    fill: none;
    stroke: var(--text-light);
    stroke-width: 1.4;
  }
</style>
</head>
<body>
<main class="sheet">
  <section class="card card-front" aria-label="Card front">
    <h1 class="front-wordmark">CORVELL</h1>
  </section>

  <section class="card card-back" aria-label="Card back">
    <svg class="back-wave" viewBox="0 0 620 354" preserveAspectRatio="none" aria-hidden="true">
      <path d="M0,192 C150,292 330,262 460,242 C540,230 590,232 620,250 V354 H0 Z" fill="var(--card-grey)"/>
      <path d="M0,148 C110,222 290,238 510,218 C420,232 290,246 160,232 C80,222 30,200 0,176 Z" fill="var(--brand-blue)"/>
    </svg>

    <div class="back-wordmark">CORVELL</div>

    <div class="holder">
      <div class="holder-name">MARTIN ASHGROVE</div>
      <div class="holder-role">CEO</div>
    </div>

    <ul class="contacts">
      <li>0208 514 3927
        <svg viewBox="0 0 14 14"><rect x="4" y="1" width="6" height="12" rx="1"/><line x1="6" y1="11" x2="8" y2="11"/></svg>
      </li>
      <li>+44 7391608254
        <svg viewBox="0 0 14 14"><path d="M3 1.5 L5.5 4 L4 5.5 C5 7.5 6.5 9 8.5 10 L10 8.5 L12.5 11 L11 12.5 C6.5 12 2 7.5 1.5 3 Z"/></svg>
      </li>
      <li>martin@corvell.co.uk
        <svg viewBox="0 0 14 14"><rect x="1" y="3" width="12" height="8"/><polyline points="1,3 7,8 13,3"/></svg>
      </li>
    </ul>
  </section>
</main>
</body>
</html>
```